Qualvine.com needs a Mobile FIRST Site

Qualvine.com is an insurance broker based in Panama City, Panama that plans to sell car and motorcycle insurance online.

We need to design a total of 5 pages (two of those are A/B test pages). The site will be responsive and will be programmed in React. We will be using Bolt Kit´s library to code Qualvine.com. Keep in mind that we are using Bolt Kit to program the site´s functions, not to create the "look and feel" of the site, that is obviously your job. You can learn more about Bolt Kit here... https://boltkit.example/

We have created wireframes for the app. Please follow and keep in mind the instructions in the wireframes. You can change things here and there as long as the core functions and goals stay intact. We have uploaded the wireframes along with the company logo and color.

We are planning to A/B test the site´s home page so we need to design two homepages. You can find homepage A and B in the wireframes provided.

We speak Spanish in Panama but you can design the site in English. We can change the text once we receive the designs.

Target Market(s)

25-45 year olds who own a car or motorcylcle and own a credit card.

Industry/Entity Type

Insurance

Font styles to use
Sans Serif

Requirements
Must have
• Follow the wireframes provided and the logo colors.
Nice to have
• Please look at the Image I´ve uploaded from DeskHarbor, use it as reference to create HomePage A.

```html
<!DOCTYPE html>
<html lang="en">
<head>
<meta charset="utf-8">
<title>Qualvine.com – Home</title>
<link rel="stylesheet" href="https://fonts.googleapis.com/css2?family=Mulish:ital,wght@0,400;0,600;0,700;0,800;1,400;1,600;1,700&display=swap">
<style>
  :root {
    --brand: #3b2a8c;
    --brand-dark: #2c1f6e;
    --accent-red: #e5484d;
    --ink: #2b2b3a;
    --muted: #8a8a99;
    --line: #e4e4ec;
    --page: #ffffff;
    --backdrop: #f3f4f7;
    --hero-a: #6f7a86;
    --hero-b: #3a4048;
    --hero-c: #1d2127;
  }
  * { box-sizing: border-box; margin: 0; padding: 0; }
  html, body { width: 1200px; height: 900px; overflow: hidden; }
  body { font-family: "Mulish", sans-serif; color: var(--ink); background: var(--page); position: relative; }

  .site-header {
    position: absolute; top: 0; left: 0; width: 1200px; height: 64px;
    background: var(--brand); display: flex; align-items: center; padding: 0 64px;
  }
  .brand-name { color: #fff; font-weight: 800; font-size: 26px; letter-spacing: -0.5px; }
  .main-nav { display: flex; gap: 36px; margin-left: 150px; }
  .main-nav a { color: #fff; font-size: 13px; font-style: italic; text-decoration: none; }
  .main-nav a.is-active::before { content: "— "; opacity: .7; }
  .search-box {
    margin-left: auto; display: flex; width: 260px; height: 32px; background: #fff;
  }
  .search-box span { flex: 1; font-size: 12px; color: var(--muted); font-style: italic; padding: 8px 10px; }
  .search-box button { width: 32px; border: 0; background: var(--brand-dark); display: flex; align-items: center; justify-content: center; }
  .cart { margin-left: 22px; position: relative; }
  .cart-count { position: absolute; top: -6px; right: -8px; width: 14px; height: 14px; border-radius: 50%; background: #fff; color: var(--brand); font-size: 9px; font-weight: 800; text-align: center; line-height: 14px; }

  .hero {
    position: absolute; top: 64px; left: 0; width: 1200px; height: 320px;
    background: linear-gradient(100deg, var(--hero-a) 0%, var(--hero-b) 55%, var(--hero-c) 100%);
  }
  .hero-copy { position: absolute; top: 58px; left: 64px; }
  .hero-title { color: #fff; font-style: italic; font-weight: 400; font-size: 30px; line-height: 1.25; width: 420px; }
  .hero-title strong { font-weight: 800; }
  .btn-outline-light {
    display: inline-block; margin-top: 26px; border: 1px solid #fff; color: #fff;
    font-size: 12px; padding: 8px 22px; font-style: italic;
  }

  .progress-card {
    position: absolute; top: 340px; left: 210px; width: 780px; height: 112px;
    background: #fff; box-shadow: 0 10px 30px rgba(30,30,60,.12);
    display: flex; justify-content: space-between; align-items: center; padding: 0 90px;
  }
  .progress-card::before {
    content: ""; position: absolute; left: 140px; right: 140px; top: 40px;
    border-top: 1px dashed #c8c8d4;
  }
  .step { position: relative; display: flex; flex-direction: column; align-items: center; gap: 8px; width: 100px; }
  .step-mark {
    width: 40px; height: 40px; border-radius: 50%; background: #fff;
    border: 2px solid #777; display: flex; align-items: center; justify-content: center;
    font-size: 17px; font-style: italic; color: #555;
  }
  .step.is-done .step-mark { background: var(--brand); border-color: var(--brand); }
  .step.is-waiting .step-mark { border-color: #c4c4cc; color: #aaa; }
  .step-label { font-size: 13px; font-weight: 700; font-style: italic; color: var(--ink); }

  .products { position: absolute; top: 478px; left: 0; width: 1200px; text-align: center; }
  .section-title { display: flex; align-items: center; justify-content: center; gap: 18px; color: var(--brand); font-size: 22px; font-weight: 600; font-style: italic; }
  .section-title::before, .section-title::after { content: ""; width: 80px; border-top: 1px solid var(--line); }
  .tabs-row { position: relative; width: 980px; margin: 16px auto 0; height: 28px; display: flex; justify-content: center; }
  .tab { display: flex; align-items: center; gap: 6px; font-size: 12px; padding: 0 18px; height: 26px; background: #eceaf3; color: var(--ink); }
  .tab.is-active { background: var(--brand); color: #fff; border-radius: 13px 0 0 13px; }
  .tab:last-child { border-radius: 0 13px 13px 0; }
  .carousel-arrow { position: absolute; top: 0; width: 26px; height: 26px; border-radius: 50%; border: 1px solid var(--line); display: flex; align-items: center; justify-content: center; }
  .carousel-arrow.prev { left: 0; } .carousel-arrow.next { right: 0; }

  .plan-grid { width: 900px; margin: 18px auto 0; display: grid; grid-template-columns: repeat(4, 1fr); gap: 26px; text-align: left; }
  .plan-card { position: relative; border: 1px solid var(--line); padding: 14px 16px 14px; height: 330px; box-shadow: 0 4px 14px rgba(30,30,60,.05); }
  .plan-card.is-featured::before { content: ""; position: absolute; top: 0; left: 0; width: 12px; height: 12px; background: var(--accent-red); }
  .plan-brand { height: 46px; display: flex; align-items: center; justify-content: center; gap: 6px; font-weight: 800; font-size: 14px; color: var(--ink); text-align: center; }
  .plan-brand i { width: 12px; height: 12px; background: var(--brand); flex: none; }
  .plan-price { text-align: center; color: var(--brand); font-weight: 700; font-size: 13px; padding: 6px 0 8px; border-bottom: 1px solid var(--line); margin: 0 20px 10px; }
  .plan-fact { font-size: 11px; font-weight: 700; margin-bottom: 7px; line-height: 1.35; }
  .plan-fact span { display: block; color: var(--brand); }
  .plan-benefits-title { font-size: 12px; font-weight: 800; margin: 12px 0 5px; }
  .plan-benefits { list-style: none; font-size: 10px; color: var(--muted); line-height: 1.6; }
  .plan-benefits li::before { content: "■ "; color: var(--brand); font-size: 7px; }
  .plan-actions { position: absolute; left: 16px; bottom: 14px; display: flex; gap: 6px; }
  .btn-buy { font-size: 11px; font-weight: 700; color: var(--brand); border: 1px solid var(--brand); padding: 4px 14px; }
  .btn-buy.is-primary { background: var(--brand); color: #fff; }
  .btn-view { width: 24px; border: 1px solid var(--brand); display: flex; align-items: center; justify-content: center; }
</style>
</head>
<body>
  <header class="site-header">
    <div class="brand-name">Qualvine</div>
    <nav class="main-nav">
      <a class="is-active" href="#">Home</a>
      <a href="#">About Us</a>
      <a href="#">Products</a>
      <a href="#">Contact Us</a>
    </nav>
    <div class="search-box">
      <span>Search...</span>
      <button aria-label="Search"><svg width="13" height="13" viewBox="0 0 14 14"><circle cx="6" cy="6" r="4.5" fill="none" stroke="#fff" stroke-width="1.8"/><line x1="9.3" y1="9.3" x2="13" y2="13" stroke="#fff" stroke-width="1.8"/></svg></button>
    </div>
    <div class="cart" aria-label="Cart">
      <svg width="26" height="22" viewBox="0 0 26 22"><path d="M1 2h4l3 12h13l3-9H7" fill="none" stroke="#fff" stroke-width="1.8" stroke-linejoin="round"/><circle cx="10" cy="19" r="1.8" fill="#fff"/><circle cx="19" cy="19" r="1.8" fill="#fff"/></svg>
      <span class="cart-count">0</span>
    </div>
  </header>

  <section class="hero" role="img" aria-label="Photo of a dark sedan driving fast on a curving road with red tail lights">
    <div class="hero-copy">
      <h1 class="hero-title">We Have <strong>Excellent Plans Available</strong> Through Reputable <strong>Auto Insurers!</strong></h1>
      <span class="btn-outline-light">Contact Us</span>
    </div>
  </section>

  <div class="progress-card">
    <div class="step is-done">
      <div class="step-mark"><svg width="16" height="12" viewBox="0 0 16 12"><path d="M1.5 6l4.5 4.5L14.5 1.5" fill="none" stroke="#fff" stroke-width="2.2"/></svg></div>
      <div class="step-label">Finished</div>
    </div>
    <div class="step">
      <div class="step-mark">2</div>
      <div class="step-label">In Progress</div>
    </div>
    <div class="step is-waiting">
      <div class="step-mark">3</div>
      <div class="step-label">Waiting</div>
    </div>
  </div>

  <section class="products">
    <h2 class="section-title">Our Products</h2>
    <div class="tabs-row">
      <span class="carousel-arrow prev"><svg width="8" height="10" viewBox="0 0 8 10"><path d="M6 1L2 5l4 4" fill="none" stroke="#888" stroke-width="1.5"/></svg></span>
      <span class="tab is-active"><svg width="12" height="9" viewBox="0 0 12 9"><path d="M1 5l2-4h6l2 4v3H1z" fill="#fff"/></svg>Cars</span>
      <span class="tab"><svg width="12" height="9" viewBox="0 0 12 9"><circle cx="2.5" cy="6.5" r="2" fill="none" stroke="#333"/><circle cx="9.5" cy="6.5" r="2" fill="none" stroke="#333"/><path d="M2.5 6.5L5 3h3l1.5 3.5" fill="none" stroke="#333"/></svg>Motorcycle</span>
      <span class="carousel-arrow next"><svg width="8" height="10" viewBox="0 0 8 10"><path d="M2 1l4 4-4 4" fill="none" stroke="#888" stroke-width="1.5"/></svg></span>
    </div>

    <div class="plan-grid">
      <article class="plan-card is-featured">
        <div class="plan-brand"><i></i>Harborline Insurance</div>
        <div class="plan-price">$150.00</div>
        <p class="plan-fact">Insurance Coverage<span>$ 10,000</span></p>
        <p class="plan-fact">Maximum Amount<span>$ 15,000</span></p>
        <p class="plan-fact">Insurance Limit<span>$ 10,000</span></p>
        <p class="plan-benefits-title">Benefits</p>
        <ul class="plan-benefits"><li>Roadside help included</li><li>Free online claims</li><li>Discounted renewals</li></ul>
        <div class="plan-actions"><span class="btn-buy">Buy Now!</span><span class="btn-view"><svg width="12" height="8" viewBox="0 0 12 8"><path d="M1 4c2-4 8-4 10 0-2 4-8 4-10 0z" fill="none" stroke="#3b2a8c"/><circle cx="6" cy="4" r="1.5" fill="#3b2a8c"/></svg></span></div>
      </article>
      <article class="plan-card">
        <div class="plan-brand"><i></i>Pinecrest Insurance</div>
        <div class="plan-price">$120.00</div>
        <p class="plan-fact">Insurance Coverage<span>$ 10,000</span></p>
        <p class="plan-fact">Maximum Amount<span>$ 15,000</span></p>
        <p class="plan-fact">Accident Limit<span>$ 10,000</span></p>
        <p class="plan-benefits-title">Benefits</p>
        <ul class="plan-benefits"><li>Roadside help included</li><li>Free online claims</li><li>Discounted renewals</li></ul>
        <div class="plan-actions"><span class="btn-buy">Buy Now!</span><span class="btn-view"><svg width="12" height="8" viewBox="0 0 12 8"><path d="M1 4c2-4 8-4 10 0-2 4-8 4-10 0z" fill="none" stroke="#3b2a8c"/><circle cx="6" cy="4" r="1.5" fill="#3b2a8c"/></svg></span></div>
      </article>
      <article class="plan-card is-featured">
        <div class="plan-brand"><i></i>Keystead Insurance Group</div>
        <div class="plan-price">$150.00</div>
        <p class="plan-fact">Insurance Coverage<span>$ 10,000</span></p>
        <p class="plan-fact">Maximum Amount<span>$ 15,000</span></p>
        <p class="plan-fact">Insurance Limit<span>$ 20,000</span></p>
        <p class="plan-benefits-title">Benefits</p>
        <ul class="plan-benefits"><li>Roadside help included</li><li>Free online claims</li><li>Discounted renewals</li></ul>
        <div class="plan-actions"><span class="btn-buy is-primary">Buy Now!</span><span class="btn-view"><svg width="12" height="8" viewBox="0 0 12 8"><path d="M1 4c2-4 8-4 10 0-2 4-8 4-10 0z" fill="none" stroke="#3b2a8c"/><circle cx="6" cy="4" r="1.5" fill="#3b2a8c"/></svg></span></div>
      </article>
      <article class="plan-card">
        <div class="plan-brand"><i></i>Brookmere Auto</div>
        <div class="plan-price">$120.00</div>
        <p class="plan-fact">Insurance Coverage<span>$ 10,000</span></p>
        <p class="plan-fact">Maximum Amount<span>$ 15,000</span></p>
        <p class="plan-fact">Accident Limit<span>$ 10,000</span></p>
        <p class="plan-benefits-title">Benefits</p>
        <ul class="plan-benefits"><li>Roadside help included</li><li>Free online claims</li><li>Discounted renewals</li></ul>
        <div class="plan-actions"><span class="btn-buy">Buy Now!</span><span class="btn-view"><svg width="12" height="8" viewBox="0 0 12 8"><path d="M1 4c2-4 8-4 10 0-2 4-8 4-10 0z" fill="none" stroke="#3b2a8c"/><circle cx="6" cy="4" r="1.5" fill="#3b2a8c"/></svg></span></div>
      </article>
    </div>
  </section>
</body>
</html>
```